Design logo, business cards and letterhead for my eye surgery (doctor's) practice

I am a young eye surgeon (Ophthalmic Surgeon) and I need business cards and letterhead designed ( I have a business card brief and a stationary brief submitted). A small logo would also be useful, or some shape that is seen on both the cards and the letterhead. I am based in Perth, Western Australia. I do some laser refractive work ie LASIK, but also other aspects of ophthalmology as well. The design should be conservative, professional and classic, but also, (as someone who sees young patients for laser surgery) a little interesting to people who refer to me and to patients who will be given my card. The details on the letterhead should be:
Dr Neil Barstow
MBBS (Hons), MMed, FRANZCO
Ophthalmic Surgeon

27 Harwick Rd, Dunmore
Western Australia 6214
Phone: (08) 9517 2046
Facsimile: (08) 9517 6281
Email: reception@neilbarstow-example.com.au
Provider No: 819024QM

The information on the cards should be the same, but with out the provider number.
On the back of the card should say-

Next Appointment________
The rooms can be accessed easily via public transport, or please feel free to park behind the premises in the designated parking bays.

Target Market(s)

General practitioners and optometrists who refer to me and patients

Industry/Entity Type

Business

Contact Information for Business Card

See above

Requirements
Nice to have
• I've attached a little photo which I thought may make a cute logo of sorts on the cards and letterhead.

```html
<!DOCTYPE html>
<html lang="en">
<head>
<meta charset="utf-8">
<title>Dr Neil Barstow – Business Card Options</title>
<link rel="stylesheet" href="https://fonts.googleapis.com/css2?family=Tinos:wght@400;700&family=Open+Sans:wght@400&family=Fredoka:wght@600&display=swap">
<style>
  :root {
    --page: #ffffff;
    --name-red: #e8301c;
    --cred-blue: #1b2fd6;
    --title-green: #5fe01c;
    --ink: #111111;
    --aqua-band: #3bb9e8;
    --aqua-light: #e9f8f8;
    --aqua-mid: #c9eeee;
    --rose-band: #fe321f;
    --rose-light: #fdeef7;
    --rose-mid: #f7b8dc;
  }
  * { margin: 0; padding: 0; box-sizing: border-box; }
  html, body { width: 1200px; height: 900px; overflow: hidden; background: var(--page); }
  .sheet { position: relative; width: 1200px; height: 900px; }

  .card { position: absolute; width: 554px; height: 368px; overflow: hidden; }
  .card--aqua { top: 42px; background: radial-gradient(ellipse at 75% 10%, #ffffff 0%, rgba(255,255,255,0) 60%), linear-gradient(160deg, var(--aqua-mid) 0%, var(--aqua-light) 45%, #ffffff 70%, var(--aqua-light) 100%); }
  .card--rose { top: 493px; height: 370px; background: radial-gradient(ellipse at 80% 85%, var(--rose-mid) 0%, rgba(247,184,220,0) 55%), linear-gradient(180deg, #ffffff 0%, var(--rose-light) 40%, #f9cde6 100%); }
  .card--front { left: 37px; }
  .card--back { left: 607px; }

  .band { position: absolute; left: 0; right: 0; bottom: 0; height: 58px; }
  .card--aqua .band { background: var(--aqua-band); }
  .card--rose .band { background: var(--rose-band); }

  .front-text { position: absolute; left: 0; width: 100%; text-align: center; white-space: nowrap; font-family: "Tinos", "Times New Roman", serif; }
  .doctor-name { top: 40px; left: 26px; font-size: 40px; font-weight: 700; letter-spacing: 0.6px; color: var(--name-red); text-shadow: 1px 1px 1px rgba(0,0,0,0.15); }
  .credentials { top: 85px; left: 26px; font-size: 21px; letter-spacing: 0.3px; color: var(--cred-blue); }
  .specialty { top: 114px; left: 26px; font-family: "Fredoka", "Arial Rounded MT Bold", sans-serif; font-size: 24px; font-weight: 600; letter-spacing: 0.8px; color: var(--title-green); }
  .address { top: 192px; font-size: 22px; letter-spacing: 0.4px; color: var(--ink); text-shadow: 0 0 3px #fff; }
  .phone { top: 223px; left: 6px; font-size: 27px; letter-spacing: 0.4px; color: var(--ink); text-shadow: 0 0 3px #fff; }
  .fax { top: 258px; left: 6px; font-size: 27px; letter-spacing: 0.4px; color: var(--ink); text-shadow: 0 0 3px #fff; }
  .email { position: absolute; left: 0; right: 0; bottom: 0; height: 58px; line-height: 58px; text-align: center; white-space: nowrap; font-family: "Open Sans", Arial, sans-serif; font-size: 24px; color: #ffffff; }

  .back-note { position: absolute; top: 146px; left: 26px; width: 515px; font-family: "Tinos", "Times New Roman", serif; font-size: 28px; letter-spacing: 0.3px; line-height: 34.5px; color: var(--ink); text-shadow: 0 0 3px #fff, 0 0 3px #fff; }
  .card--rose .back-note { top: 160px; left: 29px; }
</style>
</head>
<body>
<main class="sheet">

  <section class="card card--aqua card--front">
    <h1 class="front-text doctor-name">Dr Neil Barstow</h1>
    <p class="front-text credentials">MBBS (Hons), MMed, FRANZCO</p>
    <p class="front-text specialty">Ophthalmic Surgeon</p>
    <p class="front-text address">27 Harwick Rd, Dunmore, Western Australia 6214</p>
    <p class="front-text phone">Phone: (08) 9517 2046</p>
    <p class="front-text fax">Facsimile: (08) 9517 6281</p>
    <div class="band"><p class="email">Email: reception@neilbarstow-example.com.au</p></div>
  </section>

  <section class="card card--aqua card--back">
    <p class="back-note">Next Appointment________<br>The rooms can be accessed easily via public transport, or please feel free to park behind the premises in the designated parking bays.</p>
    <div class="band"></div>
  </section>

  <section class="card card--rose card--front">
    <h1 class="front-text doctor-name" style="top:43px">Dr Neil Barstow</h1>
    <p class="front-text credentials" style="top:88px">MBBS (Hons), MMed, FRANZCO</p>
    <p class="front-text specialty" style="top:117px">Ophthalmic Surgeon</p>
    <p class="front-text address" style="top:193px">27 Harwick Rd, Dunmore, Western Australia 6214</p>
    <p class="front-text phone" style="top:224px">Phone: (08) 9517 2046</p>
    <p class="front-text fax" style="top:260px">Facsimile: (08) 9517 6281</p>
    <div class="band"><p class="email">Email: reception@neilbarstow-example.com.au</p></div>
  </section>

  <section class="card card--rose card--back">
    <p class="back-note">Next Appointment________<br>The rooms can be accessed easily via public transport, or please feel free to park behind the premises in the designated parking bays.</p>
    <div class="band"></div>
  </section>

</main>
</body>
</html>
```